Business Card for Financial Asset Management Company

Now we are launching a new company based in Tokyo.
The company information is below;

Company Name: Talvane Management

Operations: Financial assets management, Proposing forming portfolio of assets, Consulting service, and advising to enhance your company's financial health

Corporate Colour: Japan Blue or Navy like below
http://staffpages.qorvenly.edu/mtavis/images/Slate/Teal-Slate-217.jpg

It's dark and deep, and will get to fit to our clients as our relationships last longer and longer.

Our images for this colour are "Japanese style" and "pride in our craftmanship" , and also "gentle".

Corporate Key Image: an order taker who is sincere, polite, but courageous

We don't have our logo yet so please feel free to put any symbol on your design.

Please do not hesitate about asking any questions.
Thank you :-)

Reason: We are still discussin on final decision. Thank you for your understanding.

```html
<!DOCTYPE html>
<html lang="en">
<head>
<meta charset="utf-8">
<title>Talvane Management – Business Card</title>
<link rel="stylesheet" href="https://fonts.googleapis.com/css2?family=Open+Sans:wght@300;400;600;700&display=swap">
<style>
  :root {
    --japan-blue: #0a4fb0;
    --japan-blue-deep: #083f94;
    --japan-blue-light: #1f6fd6;
    --wave-blue: #1a62c4;
    --ink: #1c1c1c;
    --name-blue: #0b3f8c;
    --role-blue: #1a6cc8;
    --rule-grey: #c9c9c9;
    --wave-grey: #e4e4e4;
    --paper: #ffffff;
    --canvas: #eef0f3;
  }
  * { box-sizing: border-box; margin: 0; padding: 0; }
  html, body { width: 1200px; height: 800px; overflow: hidden; }
  body {
    background: var(--canvas);
    font-family: "Open Sans", Arial, sans-serif;
    position: relative;
  }
  .card {
    position: absolute;
    top: 240px;
    width: 530px;
    height: 321px;
    overflow: hidden;
    box-shadow: 0 6px 18px rgba(0,0,0,.15);
  }
  /* Front side */
  .card--front {
    left: 50px;
    background: radial-gradient(ellipse at 50% 30%, var(--japan-blue-light) 0%, var(--japan-blue) 55%, var(--japan-blue-deep) 100%);
    color: var(--paper);
  }
  .card--front .wave-band {
    position: absolute;
    left: 0; right: 0; bottom: 0;
    height: 150px;
    background: linear-gradient(180deg, rgba(40,110,210,.0) 0%, var(--wave-blue) 35%, var(--japan-blue) 100%);
  }
  .front-mark {
    position: absolute;
    top: 48px; left: 0; right: 0;
    text-align: center;
  }
  .front-mark .mark-dot {
    display: block;
    width: 48px; height: 48px;
    margin: 0 auto 8px;
    border-radius: 50%;
    background: var(--paper);
  }
  .front-mark .mark-name {
    font-weight: 600;
    font-size: 26px;
    line-height: 1.05;
    color: var(--paper);
  }
  .services {
    position: absolute;
    top: 237px; left: 0; right: 0;
    text-align: center;
    font-size: 13px;
    font-weight: 600;
    letter-spacing: .1px;
  }
  .front-rule {
    position: absolute;
    top: 264px; left: 50%;
    width: 200px; margin-left: -100px;
    height: 1px;
    background: rgba(255,255,255,.6);
  }
  .website {
    position: absolute;
    top: 277px; left: 0; right: 0;
    text-align: center;
    font-size: 11px;
  }
  /* Back side */
  .card--back {
    left: 620px;
    background: var(--paper);
    color: var(--ink);
  }
  .back-mark {
    position: absolute;
    top: 36px; left: 36px;
    display: flex; align-items: center; gap: 10px;
  }
  .back-mark .mark-dot {
    width: 42px; height: 42px;
    border-radius: 50%;
    background: var(--japan-blue);
  }
  .back-mark .mark-name {
    font-weight: 600;
    font-size: 22px;
    line-height: 1.05;
    color: var(--japan-blue);
  }
  .contact {
    position: absolute;
    top: 118px; left: 88px;
    padding-left: 16px;
    border-left: 2px solid var(--rule-grey);
  }
  .contact .person { font-size: 17px; font-weight: 700; color: var(--name-blue); }
  .contact .role { font-size: 12px; color: var(--role-blue); margin-bottom: 14px; }
  .contact .line { font-size: 12.5px; line-height: 1.55; }
  .card--back .wave-band {
    position: absolute;
    left: 0; right: 0; bottom: 6px;
    height: 60px;
    background: linear-gradient(180deg, var(--paper) 0%, var(--wave-grey) 60%, var(--wave-grey) 100%);
  }
  .card--back .edge-strip {
    position: absolute;
    left: 0; right: 0; bottom: 0;
    height: 6px;
    background: var(--japan-blue-light);
  }
</style>
</head>
<body>
  <section class="card card--front" aria-label="Business card front">
    <div class="wave-band" role="img" aria-label="Japanese wave pattern band in blue tones"></div>
    <div class="front-mark">
      <span class="mark-dot"></span>
      <div class="mark-name">Talvane<br>Management</div>
    </div>
    <p class="services">Financial Assets . Proposing Porfolio . Consulting Services</p>
    <div class="front-rule"></div>
    <p class="website">www.talvanemanagement.jp</p>
  </section>

  <section class="card card--back" aria-label="Business card back">
    <div class="back-mark">
      <span class="mark-dot"></span>
      <div class="mark-name">Talvane<br>Management</div>
    </div>
    <div class="contact">
      <p class="person">Emiko Sanda</p>
      <p class="role">General Director</p>
      <p class="line">emiko.sanda@talvanemanagement.jp</p>
      <p class="line">Tel. 090 555 3141 &nbsp;|&nbsp; Fax. 090 555 2718</p>
      <p class="line">Kyobashi Kasumi Tower</p>
      <p class="line">2-7, Kyobashi 3-Chome, Chuo-ku, Tokyo 104-0031</p>
    </div>
    <div class="wave-band" role="img" aria-label="Japanese wave pattern band in light grey"></div>
    <div class="edge-strip"></div>
  </section>
</body>
</html>
```